K-DRAV Landing Page

We want to re-design our current home page on our website (www.korvadrax.com) to simplify it and reduce it down to the (3) main products / services we offer. There are too many options of where they can go and it seems to be confusing for them. Additionally, we sell a higher end software product and we want the site to appear very professional for when CFO's considering our software can be confident in its quality and the long established company that we are. Our products and services are all about optimizing manufacturing production for sheet metal stampers (primarily automotive and appliance). I am including a rough power point layout of what we are thinking along with flyers for our three main products. We want to maintain the look and feel of the sample marketing materials as much as possible but does not have to match exactly. We will be producing the video ourselves to add where the power point shows a video being. Please review our website for any additional information.

```html
<!DOCTYPE html>
<html lang="en">
<head>
<meta charset="utf-8">
<title>K-DRAV Solutions</title>
<link href="https://fonts.googleapis.com/css2?family=Anton&family=Montserrat:wght@400;500;600&display=swap" rel="stylesheet">
<style>
:root{
  --teal:#1c5a70;
  --sky:#1e93bd;
  --gold:#fdc010;
  --ink:#111111;
  --mist:#f4f4f4;
  --white:#ffffff;
  --night:#0b0b0b;
}
*{margin:0;padding:0;box-sizing:border-box}
html,body{width:795px;height:1200px;overflow:hidden;background:var(--white)}
body{position:relative;font-family:'Montserrat',sans-serif;color:var(--ink)}
.abs{position:absolute}
.display{font-family:'Anton',sans-serif;text-transform:uppercase;font-weight:400}
.brand{display:flex;align-items:center;gap:7px}
.brand-mark{width:22px;height:22px;background:var(--gold)}
.brand-name{font-family:'Anton',sans-serif;font-size:26px;color:#2b2b2b;letter-spacing:.5px;line-height:1}
.site-header .brand{left:74px;top:20px}
.tel{right:75px;top:24px;font-size:17px;font-weight:600}
.nav{left:0;top:69px;width:795px;height:49px;background:var(--teal)}
.nav ul,.foot-nav ul{list-style:none}
.nav li,.foot-nav li{position:absolute;color:var(--white);font-size:10px;font-weight:500;top:18px;white-space:nowrap}
.hero{left:0;top:118px;width:795px;height:393px;background:var(--mist)}
.hero h1{position:absolute;left:74px;top:86px;width:280px;font-size:42px;line-height:48px;letter-spacing:-1px;white-space:nowrap}
.hero p{position:absolute;left:74px;top:192px;width:286px;font-size:9.3px;line-height:17px}
.video{left:378px;top:178px;width:343px;height:270px;border-radius:17px;overflow:hidden;
  background:linear-gradient(160deg,#0a0a0a 0%,#2d3a4a 25%,#1f6fd0 45%,#cfd3d6 65%,#6d6d6d 100%)}
.play{position:absolute;left:149px;top:113px}
.card{position:absolute;top:560px;width:205px;border-radius:10px;padding:19px 13px;box-shadow:0 3px 10px rgba(0,0,0,.12)}
.card h2{font-family:'Anton',sans-serif;font-weight:400;text-transform:uppercase;font-size:15.5px;line-height:20px;margin-bottom:8px}
.card p{font-size:8px;line-height:14.2px;margin-bottom:8px}
.card .cta{font-family:'Anton',sans-serif;text-transform:uppercase;font-size:9.5px}
.card-new{left:71px;height:190px;background:var(--gold)}
.card-existing{left:296px;height:190px;background:var(--teal);color:var(--white)}
.card-products{left:520px;height:163px;background:var(--sky);color:var(--white)}
.guarantee{left:0;top:807px;width:795px;height:113px;background:var(--gold)}
.guarantee h2{position:absolute;left:77px;top:30px;font-size:31px;color:var(--teal);font-family:'Anton',sans-serif;font-weight:400}
.guarantee p{position:absolute;left:310px;top:30px;width:420px;font-family:'Anton',sans-serif;font-size:15.5px;line-height:23px;color:#173f57;text-transform:uppercase}
.contact .brand{left:74px;top:971px}
.info{position:absolute;top:960px;display:flex;gap:10px}
.icon{width:31px;height:31px;border-radius:50%;background:var(--gold);display:flex;align-items:center;justify-content:center;flex:none}
.info h3{font-family:'Anton',sans-serif;font-weight:400;font-size:12.5px;text-transform:uppercase;margin-top:0}
.info p{font-size:10px;line-height:17px}
.info .big{font-family:'Anton',sans-serif;font-size:13px}
.footer{left:0;top:1037px;width:795px;height:163px;background:radial-gradient(circle at 60% 70%,#1d1d1d,var(--night) 70%)}
.foot-nav li{top:37px}
.rule{position:absolute;left:74px;top:85px;width:648px;height:1px;background:#2c2c2c}
.copy{position:absolute;left:81px;top:113px;color:var(--white);font-size:10px}
.social{position:absolute;top:111px;width:22px;height:22px;border-radius:50%;background:var(--gold)}
</style>
</head>
<body>
<header class="site-header">
  <div class="brand abs"><span class="brand-mark"></span><span class="brand-name">K-DRAV</span></div>
  <div class="tel abs">Tel. 555-214-7390</div>
</header>
<nav class="nav abs">
  <ul>
    <li style="left:84px">About</li>
    <li style="left:146px">How We Help</li>
    <li style="left:244px">K-DRAV Software</li>
    <li style="left:348px">Transfer Simulation Service Contact</li>
    <li style="left:555px">Business Case</li>
    <li style="left:655px">Resources</li>
  </ul>
</nav>
<section class="hero abs">
  <h1 class="display">Welcome to<br>K-DRAV Solutions</h1>
  <p>At our core, we are a software company committed to providing cutting-edge simulation and optimization solutions. However, we understand that our customers have diverse needs and requirements which may not fit with buying software at this time. That’s why we offer flexible options for you to experience the power of K-DRAV.</p>
</section>
<div class="video abs" role="img" aria-label="Video still of a transfer press tooling simulation with blue stamped parts">
  <svg class="play" width="46" height="46" viewBox="0 0 46 46" aria-hidden="true">
    <circle cx="23" cy="23" r="23" fill="#fdc010" opacity=".35"/>
    <circle cx="23" cy="23" r="17" fill="#fdc010"/>
    <path d="M20 18 L28 23 L20 28 Z" fill="#111"/>
  </svg>
</div>
<section class="services">
  <article class="card card-new">
    <h2>New Tool Simulation and Optimization</h2>
    <p>Are you starting a new transfer tooling program soon? Trust the experts at K-DRAV to make it the best one you’ve ever had! Know your production rates before you build and confidently launch your tooling at the HIGHEST possible production rates!</p>
    <div class="cta">Request a Quote</div>
  </article>
  <article class="card card-existing">
    <h2>Existing Tool Optimization (With or Without CAD)</h2>
    <p>Are you at capacity in your transfer press, running your equipment harder than you’d like, or simply know you can be doing better? Our existing tool optimization service is a great way increase your production efficiency (OEE) and free up press capacity.</p>
    <div class="cta">Request a Quote</div>
  </article>
  <article class="card card-products">
    <h2>K-DRAV Software Products</h2>
    <p>Without question, our most successful customers are the ones who use the software themselves. K-DRAV Users typically see as much as 40% increase in their production rates! Hard to believe? Try it and see for yourself!</p>
    <div class="cta">Request a Quote</div>
  </article>
</section>
<section class="guarantee abs">
  <h2>OUR GAURANTEE:</h2>
  <p>You’ll make your money back in your first (5) projects or we’ll refund the entire purchase price!</p>
</section>
<section class="contact">
  <div class="brand abs"><span class="brand-mark"></span><span class="brand-name">K-DRAV</span></div>
  <div class="info" style="left:246px">
    <span class="icon"><svg width="12" height="14" viewBox="0 0 12 14"><path d="M6 0a5 5 0 0 0-5 5c0 4 5 9 5 9s5-5 5-9a5 5 0 0 0-5-5zm0 7a2 2 0 1 1 0-4 2 2 0 0 1 0 4z" fill="#111"/></svg></span>
    <div><h3>Location</h3><p>PO Box 412 · 88<br>Halvern Industrial</p></div>
  </div>
  <div class="info" style="left:402px">
    <span class="icon"><svg width="13" height="13" viewBox="0 0 24 24"><path d="M6.6 10.8a15 15 0 0 0 6.6 6.6l2.2-2.2a1 1 0 0 1 1-.25 11.4 11.4 0 0 0 3.6.57 1 1 0 0 1 1 1V20a1 1 0 0 1-1 1A17 17 0 0 1 3 4a1 1 0 0 1 1-1h3.5a1 1 0 0 1 1 1c0 1.25.2 2.45.57 3.57a1 1 0 0 1-.25 1z" fill="#111"/></svg></span>
    <div><h3>Phone</h3><p class="big">555-214-7390</p></div>
  </div>
  <div class="info" style="left:543px">
    <span class="icon"><svg width="13" height="10" viewBox="0 0 13 10"><rect width="13" height="10" rx="1" fill="#111"/><path d="M0.5 1 L6.5 5.5 L12.5 1" stroke="#fdc010" stroke-width="1.2" fill="none"/></svg></span>
    <div><h3>Email</h3><p>info@korvadraxsim.com</p></div>
  </div>
</section>
<footer class="footer abs">
  <nav class="foot-nav">
    <ul>
      <li style="left:83px">About</li>
      <li style="left:145px">How We Help</li>
      <li style="left:243px">K-DRAV Software</li>
      <li style="left:347px">Transfer Simulation Service Contact</li>
      <li style="left:554px">Business Case</li>
      <li style="left:654px">Resources</li>
    </ul>
  </nav>
  <div class="rule"></div>
  <div class="copy">© Copyright 2024 K-DRAV Solutions. All Rights Reserved.</div>
  <span class="social" style="left:604px"></span>
  <span class="social" style="left:636px"></span>
  <span class="social" style="left:667px"></span>
  <span class="social" style="left:698px"></span>
</footer>
</body>
</html>
```